Criação de Power Point Slide Mestre para Rocha & Vento
" A Lunavix atua como desenvolvedora e estruturadora de soluções energéticas. É responsável pela prospecção de clientes, análise técnica e regulatória, validação de faturas, estruturação do modelo econômico e coordenação do pré-projeto. A implantação, financiamento, tecnologia e operação dos sistemas são executados por parceiros estratégicos especializados, sob um modelo de longo prazo baseado em disponibilidade, performance e economia para o cliente final. "

```html
<!DOCTYPE html>
<html lang="pt-BR">
<head>
<meta charset="utf-8">
<title>Lunavix — Números</title>
<link href="https://fonts.googleapis.com/css2?family=Montserrat:wght@400;500;600;700&display=swap" rel="stylesheet">
<style>
  :root {
    --backdrop: #9b9ea3;
    --paper: #ffffff;
    --navy: #1c2857;
    --blue: #1f4fa6;
    --sky: #4aa3df;
    --orange: #f5a71d;
    --text: #4a4f5c;
    --muted: #8a8f99;
    --rule: #cfd3da;
  }
  * { box-sizing: border-box; margin: 0; padding: 0; }
  html, body { width: 1200px; height: 1200px; overflow: hidden; }
  body {
    background: var(--backdrop);
    font-family: "Montserrat", sans-serif;
    position: relative;
  }
  .slide {
    position: absolute;
    left: 24px; top: 276px;
    width: 1152px; height: 648px;
    background: var(--paper);
    overflow: hidden;
  }
  .slide__photo { position: absolute; left: 0; top: 0; }
  .brand {
    position: absolute; left: 972px; top: 50px;
    display: flex; align-items: center; gap: 8px;
    font-weight: 700; font-size: 24px; color: var(--blue);
    letter-spacing: -0.3px;
  }
  .brand__dot { width: 22px; height: 22px; border-radius: 50%; background: var(--orange); }
  .deco { position: absolute; left: 0; top: 0; }
  .headline {
    position: absolute; left: 463px; top: 106px; width: 420px;
    font-weight: 700; font-size: 30px; line-height: 1.22; color: var(--navy);
  }
  .headline em { font-style: normal; color: var(--orange); }
  .intro {
    position: absolute; left: 463px; top: 204px; width: 460px;
    font-size: 17px; line-height: 1.5; color: var(--text);
  }
  .stats { position: absolute; left: 487px; top: 322px; list-style: none; }
  .stat { display: flex; align-items: center; gap: 18px; margin-bottom: 26px; }
  .stat__icon {
    width: 70px; height: 70px; border-radius: 8px; background: var(--blue);
    display: flex; align-items: center; justify-content: center;
  }
  .stat__value { font-size: 25px; font-weight: 500; color: var(--navy); line-height: 1.1; }
  .stat__label { font-size: 16px; font-weight: 500; color: var(--orange); margin-top: 2px; }
  .footer__rule {
    position: absolute; left: 487px; top: 608px; width: 620px; height: 1px; background: var(--rule);
  }
  .footer__site, .footer__page {
    position: absolute; top: 622px; font-size: 12px; letter-spacing: 3px; color: var(--muted);
  }
  .footer__site { left: 487px; }
  .footer__page { right: 44px; }
  .footer__page b { color: var(--orange); font-weight: 700; }
</style>
</head>
<body>
  <section class="slide">
    <svg class="slide__photo" width="460" height="648" viewBox="0 0 460 648">
      <defs>
        <linearGradient id="photoTone" x1="0" y1="0" x2="1" y2="1">
          <stop offset="0" stop-color="#2d4f86"/>
          <stop offset="0.45" stop-color="#a9b4c2"/>
          <stop offset="1" stop-color="#5a4a42"/>
        </linearGradient>
      </defs>
      <polygon role="img" aria-label="Fotografia de dois profissionais de negócios analisando um tablet em frente a edifícios corporativos"
        points="0,0 216,0 420,220 420,648 0,648" fill="url(#photoTone)"/>
      <line x1="216" y1="0" x2="420" y2="220" stroke="var(--blue)" stroke-width="3"/>
      <line x1="232" y1="0" x2="430" y2="214" stroke="var(--blue)" stroke-width="1.5" opacity="0.6"/>
    </svg>

    <div class="brand"><span class="brand__dot"></span>lunavix</div>

    <svg class="deco" width="1152" height="648" viewBox="0 0 1152 648" aria-hidden="true">
      <circle cx="1020" cy="378" r="132" fill="var(--orange)"/>
      <circle cx="1150" cy="330" r="108" fill="var(--sky)"/>
    </svg>

    <h1 class="headline">Números que traduzem <em>nossa</em> Experiência</h1>
    <p class="intro">Nossos resultados refletem credibilidade, segurança e impacto no futuro sustentável. Pois somos referência em ativos de energia</p>

    <ul class="stats">
      <li class="stat">
        <span class="stat__icon">
          <svg width="40" height="40" viewBox="0 0 40 40" aria-hidden="true">
            <rect x="5" y="8" width="30" height="27" rx="3" fill="none" stroke="var(--orange)" stroke-width="3"/>
            <line x1="5" y1="16" x2="35" y2="16" stroke="var(--orange)" stroke-width="3"/>
            <line x1="13" y1="4" x2="13" y2="11" stroke="var(--orange)" stroke-width="3"/>
            <line x1="27" y1="4" x2="27" y2="11" stroke="var(--orange)" stroke-width="3"/>
          </svg>
        </span>
        <div><div class="stat__value">10 anos</div><div class="stat__label">no Setor Elétrico</div></div>
      </li>
      <li class="stat">
        <span class="stat__icon">
          <svg width="40" height="40" viewBox="0 0 40 40" aria-hidden="true">
            <path d="M20 5a11 11 0 0 0-6.5 19.8V29h13v-4.2A11 11 0 0 0 20 5z" fill="var(--orange)"/>
            <rect x="14" y="31" width="12" height="3" rx="1" fill="var(--orange)"/>
            <rect x="16" y="35" width="8" height="2.5" rx="1" fill="var(--orange)"/>
          </svg>
        </span>
        <div><div class="stat__value">+2GW</div><div class="stat__label">Comercializados</div></div>
      </li>
    </ul>

    <div class="footer__rule"></div>
    <span class="footer__site">WWW.LUNAVIX.COM.BR</span>
    <span class="footer__page">PÁGINA <b>04</b></span>
  </section>
</body>
</html>
```